Velora Pedal Journeys Brochure

We need an informational brochure designed to display all of our cycling tours for the 2019 season. The majority of text and images can be pulled from our website - www.velorapedaljourneys.com

We would like to use the colors red (#242424), Grey, and White

```html
<!DOCTYPE html>
<html lang="en">
<head>
<meta charset="utf-8">
<title>Velora Pedal Journeys – Itinerary and Details</title>
<link href="https://fonts.googleapis.com/css2?family=Oswald:wght@500;600;700&family=Roboto+Condensed:wght@300;400;700&display=swap" rel="stylesheet">
<style>
  :root {
    --brand-red: #b22234;
    --panel-white: #ffffff;
    --ink: #2b2b2b;
    --grey: #6d6e71;
    --photo-rock: #9a5a3c;
    --photo-sky: #7d95ad;
    --map-green: #cfe2c4;
  }
  * { box-sizing: border-box; margin: 0; padding: 0; }
  html, body { width: 848px; height: 1200px; overflow: hidden; }
  body {
    position: relative;
    background: var(--brand-red);
    font-family: "Roboto Condensed", "Arial Narrow", sans-serif;
    font-weight: 300;
    color: var(--ink);
  }
  .panel { position: absolute; background: var(--panel-white); }
  .panel-left { left: 33px; top: 32px; width: 387px; height: 890px; }
  .panel-left-lower { left: 33px; top: 918px; width: 258px; height: 174px; }
  .panel-right { left: 427px; top: 32px; width: 388px; height: 890px; }

  .day { position: absolute; font-size: 11.6px; line-height: 15.3px; text-align: justify; }
  .col-left { left: 41px; width: 370px; }
  .col-right { left: 436px; width: 370px; }
  .day-title {
    font-family: "Oswald", sans-serif; font-weight: 600; font-size: 12.6px;
    line-height: 16px; color: var(--brand-red); text-transform: uppercase; letter-spacing: .1px;
  }
  .day p { margin: 0; }
  b { font-weight: 400; }

  .spacer { float: right; width: 0; }
  .photo { float: right; clear: right; margin-left: 8px; }
  .photo-mesa { width: 158px; height: 86px;
    background: linear-gradient(180deg, var(--photo-sky) 0%, #b7a48d 45%, var(--photo-rock) 100%); }
  .photo-rim { width: 141px; height: 129px;
    background: linear-gradient(135deg, #c56a38 0%, #5a4030 55%, #2f2620 100%); }
  .photo-trail { width: 120px; height: 137px;
    background: linear-gradient(160deg, #8c8a7e 0%, #6b6a5c 50%, #4a4a40 100%); }
  .photo-canyon { width: 147px; height: 72px;
    background: linear-gradient(180deg, #9db3c8 0%, #d28a5a 45%, #b05a34 100%); }

  .details { position: absolute; font-size: 11.6px; line-height: 15.3px; }
  .details dt, .details dd { display: inline; }
  .details dt { font-weight: 400; }
  .details .gap { margin-top: 4px; }

  .rule { position: absolute; height: 1px; background: var(--brand-red); }

  .route-map { position: absolute; left: 296px; top: 926px; width: 518px; height: 166px;
    background: linear-gradient(120deg, #dcebd4 0%, var(--map-green) 50%, #bdd8b0 100%);
    border: 3px solid #f2f2f2; }

  .footer-title { position: absolute; left: 94px; top: 1119px;
    font-family: "Oswald", sans-serif; font-weight: 700; font-size: 40px; line-height: 44px;
    color: var(--panel-white); transform: scaleX(.86); transform-origin: left top; }
  .brand-block { position: absolute; left: 516px; top: 1100px; width: 332px; height: 100px;
    background: var(--panel-white); }
  .brand-mark { position: absolute; left: 40px; top: 6px; width: 76px; height: 76px;
    border-radius: 50%; border: 3px solid var(--grey); }
  .brand-name { position: absolute; left: 124px; top: 12px; width: 200px;
    font-family: "Oswald", sans-serif; font-weight: 600; font-size: 26px; line-height: 30px;
    color: var(--brand-red); }
</style>
</head>
<body>
  <div class="panel panel-left"></div>
  <div class="panel panel-left-lower"></div>
  <div class="panel panel-right"></div>

  <!-- Day 1 -->
  <section class="day col-left" style="top:40px">
    <div class="spacer" style="height:170px"></div>
    <div class="photo photo-mesa" role="img" aria-label="Riders with mountain bikes on a mesa above red rock canyons"></div>
    <h2 class="day-title">Day 1: Gooseberry Mesa</h2>
    <p><b>Starting/Meeting point:</b> 8am at Las Vegas Meeting Point TBD</p>
    <p>Gooseberry Mesa is regarded to be one of the best technical trails in the world, and is the perfect starting point for your adventure. On this singletrack trail you will find yourself surrounded by incredible views of red rock mesas, water carved canyons, and the massive sentinel spires of Zion National Park. The mesa offers a number of marked trail options with ample bailouts, allowing for some serious flexibility when determining the length and difficulty of today’s ride. While you won’t face any major elevation gains, your balance, burst, and reactions will be put to the test. After a full day of glory, we’ll head back to our hotel in Springdale, to celebrate a successful first day with an included dinner at the Red Cliff Brewing House.</p>
  </section>
  <dl class="details" style="left:41px;top:229px">
    <div><dt>Route:</dt> <dd>Gooseberry Mesa – The Big Loop</dd></div>
    <div><dt>Distance:</dt> <dd>13.1 miles</dd></div>
    <div><dt>Elevation Gain:</dt> <dd>570ft / 570ft</dd></div>
    <div class="gap"><dt>Accommodation:</dt> <dd>Canyon Rest Inn Zion</dd></div>
  </dl>
  <div class="rule" style="left:41px;top:301px;width:370px"></div>

  <!-- Day 2 -->
  <section class="day col-left" style="top:310px">
    <div class="spacer" style="height:159px"></div>
    <div class="photo photo-rim" role="img" aria-label="Mountain biker descending a red rock trail at sunset"></div>
    <h2 class="day-title">Day 2 - Hurricane Rim</h2>
    <p>Our main route today combines the Hurricane Rim Trail, Goulds Rim, and JEM Trails to form an epic 20 mile singletrack circuit. This ride features more of the spectacular desert and canyon vistas typical of the region, including views of Zion. Although there are a couple of easy climbs, this trail maintains a heavy downhill flow, culminating in the incredibly fast, and fun JEM descent. Following the ride, rejoin your group to recharge with an included lunch in Hurricane. If you’re still feeling hungry after lunch, take a bite out of the Whole Guacamole. This route features 11 miles of fantastic singletrack, slickrock, and technical features, with spectacular views of West Temple, Mount Kinesava, Pine Valley Mountains, and St George.</p>
  </section>
  <dl class="details" style="left:41px;top:480px">
    <div><dt>Route:</dt> <dd>Hurricane Rim Loop – Regional Epic</dd></div>
    <div><dt>Distance:</dt> <dd>23.7 miles</dd></div>
    <div><dt>Elevation Gain:</dt> <dd>1937ft / 1935ft</dd></div>
    <div class="gap"><dt>Afternoon Extension:</dt> <dd>The Whole Guacamole</dd></div>
    <div><dt>Distance:</dt> <dd>11 miles</dd></div>
    <div><dt>Elevation Gain:</dt> <dd>602ft / 602ft</dd></div>
    <div class="gap"><dt>Accommodation:</dt> <dd>Canyon Rest Inn Zion</dd></div>
  </dl>
  <div class="rule" style="left:41px;top:602px;width:370px"></div>

  <!-- Day 3 -->
  <section class="day col-left" style="top:610px">
    <h2 class="day-title">Day 3 - Thunder Mountain</h2>
    <p>There are two approaches to the main feature of today’s ride, the Thunder Mountain Trail. Route 1 represents a longer, full loop of the area before finishing with the Thunder Mountain Trail. This route begins with a mellow 5.5 mile climb on a paved bike path before opening up into a mountain prairie, and a 2 mile ride along a dirt road to the Thunder Mountain Trailhead. Route 2 gets straight to the point, beginning directly at the trailhead.</p>
    <p>Located just outside Bryce National Park, you’ll be treated to amazing views of the striking white and orange cliffs, and hoodoos. At 8000ft the ups and downs at the beginning will have you breathing heavy before finding the downhill flow later in the ride. The trail is mostly smooth hard pack, and while there aren’t too many technical sections or drops, there are a few loose, steep switchbacks which will be sure to have you white knuckling. Its all worth it, as the last couple miles are a balls to the wall downhill, on smooth single track.</p>
    <p>If that downhill had you feeling squirrelly, the afternoon extension is another singletrack downhill from Brian Head Peak to Panguitch. To no one’s surprise, this ride features incredible views in every direction as you climb above the timberline, highlighted by the appearance of Cedar Breaks National Monument to the South. As you drop into the drainage, you’ll have the opportunity to bomb it to the bottom in another fast and fun downhill.</p>
  </section>
  <dl class="details" style="left:41px;top:923px">
    <div><dt>Main Route Option 1:</dt> <dd>Thunder Mountain Loop</dd></div>
    <div><dt>Distance:</dt> <dd>16 miles</dd></div>
    <div><dt>Elevation Gain:</dt> <dd>1630ft / 1630ft</dd></div>
    <div class="gap"><dt>Main Route Option 2:</dt> <dd>Thunder Mountain Trail</dd></div>
    <div><dt>Distance:</dt> <dd>8.1 miles</dd></div>
    <div><dt>Elevation Gain:</dt> <dd>659ft / 1681ft</dd></div>
    <div class="gap"><dt>Afternoon Extension:</dt> <dd>Bunker Creek</dd></div>
    <div><dt>Distance:</dt> <dd>11 miles</dd></div>
    <div><dt>Elevation Gain:</dt> <dd>331ft / 2932ft</dd></div>
    <div class="gap"><dt>Accommodation:</dt> <dd>Summit Pines Lodge</dd></div>
  </dl>

  <!-- Day 4 -->
  <section class="day col-right" style="top:40px">
    <div class="spacer" style="height:277px"></div>
    <div class="photo photo-trail" role="img" aria-label="Mountain biker riding a rocky technical section"></div>
    <h2 class="day-title">Day 4 - Virgin River Rim Trail Pt 1</h2>
    <p>On today’s ride, we tackle the first section of the 32 mile long Virgin River Rim Trail. A tributary of the Colorado River, the Virgin River has carved through the red sandstone of Zion National Park for over 13 million years, creating some of the most unforgettable scenery in the world.</p>
    <p>The trail base is mostly hard pack dirt, but also features a number of more rocky, technical sections. As you climb the ridfeline, the ride begins with a high altitude alpine single track trail winding through forests of pine, fir, and aspen. From 6000 ft above the valley floor, you’ll encounter incredible views of the Pink Cliffs, the surrounding valley, and the Virgin River as it breaks towards Zion.</p>
    <p>Nearing Cascade Falls, you’l be faced with a decent uphill, and rewarded with more amazing viewpoints overlooking Navajo Lake. From here you can take a break from the saddle with a quick half mile hike to Cascade Falls before beginning the second segment en route to Te Ah Campground. The second segment will see two moderate climbs, and a number of even more stunning sights before a long descent to our finish point.</p>
    <p>Following this long day on the trail, we’ll return to Brianhead to relax, and recover with an included dinner and massage.</p>
  </section>
  <dl class="details" style="left:436px;top:335px">
    <div><dt>Main Route 1:</dt> <dd>Strawberry Point to Cascade Falls</dd></div>
    <div><dt>Distance:</dt> <dd>11 miles</dd></div>
    <div><dt>Elevation Gain:</dt> <dd>1952ft / 1283ft</dd></div>
    <div class="gap"><dt>Main Route 2:</dt> <dd>Cascade Falls to Te Ah Campground</dd></div>
    <div><dt>Distance:</dt> <dd>7 miles</dd></div>
    <div><dt>Elevation Gain:</dt> <dd>443ft / 853ft</dd></div>
    <div class="gap"><dt>Accommodation:</dt> <dd>Summit Pines Lodge</dd></div>
  </dl>
  <div class="rule" style="left:436px;top:460px;width:370px"></div>

  <!-- Day 5 -->
  <section class="day col-right" style="top:466px">
    <div class="spacer" style="height:172px"></div>
    <div class="photo photo-canyon" role="img" aria-label="Amphitheater of orange hoodoos in a canyon"></div>
    <h2 class="day-title">Day 5 - Virgin River Rim Trail Pt 2</h2>
    <p>We pick up where we left off yesterday, as we return to conquer the second half of the Virgin River Rim Trail. While yesterday’s ride was largely spent above the ridgeline on high altitude mesas, today’s section dives into a dense forest of fir and aspen. Gradual elevation changes in this section give way to a fast and thickly forested three mile downhill.</p>
    <p>Our afternoon extension is an absolute classic downhill trail intended for experts. Serving as one of the courses in the Southern Gravity Race Series, the Dark Hollow sees steep descents, rocky switchbacks, and some challenging technical sections. With a total descent of 4600ft over 12 miles, this trail provides another opportunity to hit some hard and fast downhills.</p>
  </section>
  <dl class="details" style="left:436px;top:641px">
    <div><dt>Main Route:</dt> <dd>Te-Ah CG to Woods Ranch</dd></div>
    <div><dt>Distance:</dt> <dd>10.6 miles</dd></div>
    <div><dt>Elevation Gain:</dt> <dd>650ft / 1609ft</dd></div>
    <div class="gap"><dt>Accommodation:</dt> <dd>Summit Pines Lodge</dd></div>
  </dl>
  <div class="rule" style="left:436px;top:714px;width:370px"></div>

  <!-- Day 6 -->
  <section class="day col-right" style="top:722px">
    <h2 class="day-title">Day 6 - Brianhead Mountain Bike Park</h2>
    <p>The Mountain Bike Park in Brianhead is truly one of the most unique mountain biking experiences available in the country. Referred to as “Downhill of the Gods,” by Trailside Journal, the park utilizes a combined chairlift, and shuttle service allowing access to 5000ft descents, and over 100 miles of trails designed by the legendary Flowline Trail Builders crew. With trails ranging from easy to advanced, and a plethora of freestyle, downhill, and technical features, you’ll be able to create the adventure of a lifetime. Rejoin your group in the afternoon to celebrate the memories, sore saddles, and friendships formed over a tasty meal and a cold beer.</p>
    <p><b>Optional Post Night:</b> Desert Palm Resort</p>
  </section>

  <div class="route-map" role="img" aria-label="Route map from Desert Palm Resort north to Canyon Rest Inn Zion and Summit Pines Lodge"></div>

  <h1 class="footer-title">ITINERARY AND DETAILS</h1>
  <div class="brand-block">
    <div class="brand-mark"></div>
    <div class="brand-name">Velora Pedal Journeys</div>
  </div>
</body>
</html>
```